High impact classy folder for an HVAC and Electrical contractor

We need a folder designed. It needs to be high impact and classy with a rich look to it. We want to cement our branding via the use of the folder so the look will need to have impact with use of our logo and colors.

We want to pull the entire brand look and feel together with this folder. We are going to be making other marketing materials and this is the start of a much larger project. In the ideal situation the winning desginer will continue on with the rest of the projects because they will know how to apply the brand look.

We want to give our local company the feel of a national franchise. Wherein the brand is very prominent and is repeated over and over again.

Use of logo and color scheme will be important.

We like dark backgrounds because they really make the logo pop.

Target Market(s)

homeowners

Font styles to use
Serif

Requirements
Must have
• Logo prominent on the front
• Our Tag Line:
• The Best Way To Live In New Jersey Is With Hearthline"
• On the inside pockets:
• Our Phone number: 973-555-0184
• A message to our customers:
• We want to thank you for choosing Hearthline Partners today
• Our name says it all, because for over 30 years we have prided ourselves on delivering the best service and exceeding our customers' expectations everyday. Whether you need something fixed, replaced or upgraded, no matter how large or small, the dedicated and experts at Hearthline Partners are here to take care of you. Delivering the right solution for you the first time- everytime - and ensuring you are always 100% satisfied. If for any reason you want to speak with us, please do not hesitate to call or email. Thank you again for choosing Hearthline Partners.
• On the rear: a graphic that says 24-7 service
• A list of other services we provide:
• Solar
• Generators
• Home Security
• Home Automation
• Home Inspection
• Energy Audits
• 1 Day Bathroom remodles
• Basement Waterproofing
• Garage Doors
• Home Theaters
Nice to have
• I added photos of a flyer and of a mobile website to give an idea of the color scheme as well

```html
<!DOCTYPE html>
<html lang="en">
<head>
<meta charset="utf-8">
<title>Hearthline Partners – Presentation Folder</title>
<link rel="stylesheet" href="https://fonts.googleapis.com/css2?family=Cinzel:wght@400;700&family=Open+Sans:ital,wght@0,700;1,700&display=swap">
<style>
  :root {
    --page-bg: #e9d3d5;
    --brand-red: #a51c24;
    --brand-red-light: #b8262e;
    --brand-orange: #f08a2c;
    --brand-cream: #f6dfae;
    --band-white: #f4f4f4;
    --band-grey: #cfcfcf;
    --text-white: #ffffff;
  }
  * { box-sizing: border-box; margin: 0; padding: 0; }
  html, body { width: 1200px; height: 847px; overflow: hidden; }
  body {
    background: var(--page-bg);
    display: flex;
    align-items: center;
    justify-content: center;
  }
  .folder-spread {
    display: flex;
    gap: 0;
    box-shadow: 0 18px 40px rgba(90, 30, 35, 0.25);
  }
  .folder-panel { width: 500px; height: 680px; display: block; }
  .service-label {
    font-family: "Open Sans", Arial, sans-serif;
    font-style: italic;
    font-weight: 700;
    fill: var(--text-white);
    font-size: 12px;
  }
  .badge-number {
    font-family: "Open Sans", Arial, sans-serif;
    font-style: italic;
    font-weight: 700;
    font-size: 34px;
    fill: var(--text-white);
  }
  .badge-caption {
    font-family: "Open Sans", Arial, sans-serif;
    font-weight: 700;
    font-size: 12px;
    fill: var(--text-white);
  }
  .brand-name {
    font-family: "Cinzel", Georgia, serif;
    font-weight: 700;
    font-size: 50px;
    fill: var(--brand-cream);
    letter-spacing: 1px;
  }
  .tagline {
    font-family: "Cinzel", Georgia, serif;
    font-weight: 400;
    font-size: 14.5px;
    fill: var(--brand-red);
    letter-spacing: 0.3px;
  }
</style>
</head>
<body>
<main class="folder-spread">

  <!-- Back cover -->
  <svg class="folder-panel back-cover" viewBox="0 0 500 680" xmlns="http://www.w3.org/2000/svg">
    <defs>
      <linearGradient id="solar-tone" x1="0" y1="0" x2="1" y2="1">
        <stop offset="0" stop-color="#f2b35a"/><stop offset="1" stop-color="#3d5a7a"/>
      </linearGradient>
      <linearGradient id="automation-tone" x1="0" y1="0" x2="1" y2="1">
        <stop offset="0" stop-color="#b9cbe0"/><stop offset="1" stop-color="#5f6f86"/>
      </linearGradient>
      <linearGradient id="bathroom-tone" x1="0" y1="0" x2="1" y2="1">
        <stop offset="0" stop-color="#e8e6e2"/><stop offset="1" stop-color="#8a8884"/>
      </linearGradient>
    </defs>

    <rect class="panel-bg" width="500" height="680" fill="var(--brand-red)"/>

    <g class="service-thumbnails">
      <g role="img" aria-label="Photo of solar panels at sunset">
        <rect x="65" y="45" width="90" height="90" rx="14" transform="rotate(45 110 90)" fill="url(#solar-tone)" stroke="var(--text-white)" stroke-width="6"/>
      </g>
      <g role="img" aria-label="Photo of a tablet controlling a smart home">
        <rect x="205" y="45" width="90" height="90" rx="14" transform="rotate(45 250 90)" fill="url(#automation-tone)" stroke="var(--text-white)" stroke-width="6"/>
      </g>
      <g role="img" aria-label="Photo of a remodeled bathroom">
        <rect x="345" y="45" width="90" height="90" rx="14" transform="rotate(45 390 90)" fill="url(#bathroom-tone)" stroke="var(--text-white)" stroke-width="6"/>
      </g>
    </g>

    <g class="swoosh">
      <path d="M0 250 Q260 262 500 150 L500 172 Q260 292 0 278 Z" fill="var(--band-white)"/>
      <path d="M0 278 Q260 292 500 172 L500 180 Q260 302 0 288 Z" fill="var(--brand-orange)"/>
    </g>

    <g class="service-badge" transform="translate(250 335)">
      <circle r="50" fill="var(--brand-red)" stroke="var(--text-white)" stroke-width="4"/>
      <path d="M-34 -30 A45 45 0 0 1 38 -22" fill="none" stroke="var(--brand-orange)" stroke-width="5" stroke-linecap="round"/>
      <text class="badge-number" x="0" y="6" text-anchor="middle">24/7</text>
      <text class="badge-caption" x="0" y="24" text-anchor="middle">Customer</text>
      <text class="badge-caption" x="0" y="38" text-anchor="middle">Service</text>
    </g>

    <g class="service-list">
      <line x1="20" y1="420" x2="480" y2="420" stroke="var(--brand-orange)" stroke-width="1.5"/>
      <rect x="206" y="406" width="88" height="24" fill="var(--brand-red-light)" stroke="var(--brand-orange)" stroke-width="1.5"/>
      <text class="service-label" x="250" y="423" text-anchor="middle">Services</text>

      <g class="service-row" fill="var(--brand-red-light)">
        <rect x="20" y="440" width="88" height="36"/><rect x="114" y="440" width="88" height="36"/>
        <rect x="208" y="440" width="88" height="36"/><rect x="302" y="440" width="88" height="36"/>
        <rect x="396" y="440" width="88" height="36"/>
        <rect x="20" y="482" width="88" height="36"/><rect x="114" y="482" width="88" height="36"/>
        <rect x="208" y="482" width="88" height="36"/><rect x="302" y="482" width="88" height="36"/>
        <rect x="396" y="482" width="88" height="36"/>
      </g>
      <g class="service-dividers" fill="var(--brand-orange)">
        <rect x="17" y="440" width="3" height="78"/><rect x="111" y="440" width="3" height="78"/>
        <rect x="205" y="440" width="3" height="78"/><rect x="299" y="440" width="3" height="78"/>
        <rect x="393" y="440" width="3" height="78"/><rect x="484" y="440" width="3" height="78"/>
      </g>

      <text class="service-label" x="64" y="462" text-anchor="middle">Solar</text>
      <text class="service-label" x="158" y="462" text-anchor="middle">Generators</text>
      <text class="service-label" x="252" y="455" text-anchor="middle">Home</text>
      <text class="service-label" x="252" y="469" text-anchor="middle">Security</text>
      <text class="service-label" x="346" y="455" text-anchor="middle">Home</text>
      <text class="service-label" x="346" y="469" text-anchor="middle">Automation</text>
      <text class="service-label" x="440" y="455" text-anchor="middle">Home</text>
      <text class="service-label" x="440" y="469" text-anchor="middle">Inspection</text>

      <text class="service-label" x="64" y="497" text-anchor="middle">Energy</text>
      <text class="service-label" x="64" y="511" text-anchor="middle">Audits</text>
      <text class="service-label" x="158" y="497" text-anchor="middle" font-size="11">Basement</text>
      <text class="service-label" x="158" y="511" text-anchor="middle" font-size="11">Waterproofing</text>
      <text class="service-label" x="252" y="497" text-anchor="middle">Garage</text>
      <text class="service-label" x="252" y="511" text-anchor="middle">Doors</text>
      <text class="service-label" x="346" y="497" text-anchor="middle">Home</text>
      <text class="service-label" x="346" y="511" text-anchor="middle">Theaters</text>
      <text class="service-label" x="440" y="497" text-anchor="middle" font-size="10.5">1 Day Bathroom</text>
      <text class="service-label" x="440" y="511" text-anchor="middle" font-size="10.5">remodles</text>
    </g>

    <g class="bottom-bands">
      <rect x="0" y="556" width="500" height="22" fill="var(--band-white)"/>
      <rect x="0" y="578" width="500" height="4" fill="var(--band-grey)"/>
      <rect x="0" y="636" width="500" height="20" fill="var(--band-white)"/>
      <rect x="0" y="656" width="500" height="6" fill="var(--brand-orange)"/>
    </g>
  </svg>

  <!-- Front cover -->
  <svg class="folder-panel front-cover" viewBox="0 0 500 680" xmlns="http://www.w3.org/2000/svg">
    <defs>
      <linearGradient id="crew-tone" x1="0" y1="0" x2="1" y2="0">
        <stop offset="0" stop-color="#d9a24a"/><stop offset="0.4" stop-color="#e9e4dc"/><stop offset="1" stop-color="#c9a36a"/>
      </linearGradient>
    </defs>

    <rect class="panel-bg" width="500" height="680" fill="var(--brand-red)"/>

    <path role="img" aria-label="Photo of a team of contractors in hard hats" d="M0 0 H500 V128 Q250 118 0 158 Z" fill="url(#crew-tone)"/>

    <g class="swoosh">
      <path d="M0 158 Q250 118 500 128 L500 146 Q250 138 0 178 Z" fill="var(--band-white)"/>
      <path d="M0 178 Q250 138 500 146 L500 153 Q250 146 0 186 Z" fill="var(--brand-orange)"/>
    </g>

    <g class="brand-mark">
      <text class="brand-name" x="250" y="320" text-anchor="middle">Hearthline</text>
      <text class="brand-name" x="250" y="378" text-anchor="middle">Partners</text>
    </g>

    <g class="tagline-band">
      <rect x="0" y="572" width="500" height="28" fill="var(--band-white)"/>
      <text class="tagline" x="250" y="591" text-anchor="middle">The Best Way To Live In New Jersey Is With Hearthline"</text>
      <rect x="0" y="604" width="500" height="6" fill="var(--brand-orange)"/>
    </g>
  </svg>

</main>
</body>
</html>
```